Simon & Lorna's Yuletide Unwind Bash

Invitation to a party 60-80 people at a private residence. Age range 30-40s.

Themes: summer/casual/Australian backyard/local community

**For delivery via both email and printed copy**
Would like one document suitable for both purposes or two versions for electronic or paper invitation. I will arrange printing so please prepare it in a suitable format.

Specimen text attached. Address and phone contact to follow by message with successful bidder

Thanks!
Simon

Target Market(s)

Locals, friends. Party attendees will typicaly be parents in their forties who who be leaving the kids at home for a relaxed party night, and walking home afterward

Industry/Entity Type

Community

Font styles to use
Sans Serif

Requirements
Should not have
• Cliche Australiana imagery. No kangaroos etc

```html
<!DOCTYPE html>
<html lang="en">
<head>
<meta charset="utf-8">
<title>Simon &amp; Lorna's Yuletide Unwind Bash – Invitation</title>
<link rel="stylesheet" href="https://fonts.googleapis.com/css2?family=Roboto+Condensed:wght@300;400&family=Permanent+Marker&family=Kaushan+Script&family=Sue+Ellen+Francisco&display=swap">
<style>
  :root {
    --page: #ffffff;
    --sea-deep: #1f7f9c;
    --sea-mid: #1ea3b8;
    --sea-light: #2cbcc6;
    --foam: #e9f4f2;
    --sand: #d8c2a2;
    --sand-dark: #c9ae8a;
    --text-light: #ffffff;
    --text-dark: #1a1a1a;
    --title: #eef5f7;
  }
  * { margin: 0; padding: 0; box-sizing: border-box; }
  html, body { width: 794px; height: 1200px; overflow: hidden; background: var(--page); }
  .canvas { position: relative; width: 794px; height: 1200px; }

  .card {
    position: absolute; left: 10px; width: 776px; height: 364px; overflow: hidden;
    font-family: "Roboto Condensed", "Arial Narrow", sans-serif; font-weight: 300;
    color: var(--text-light); text-align: center;
  }
  .card--front { top: 6px; }
  .card--back { top: 398px; }
  .card--single { top: 792px; width: 772px; }

  .beach-scene {
    position: absolute; inset: 0;
    background: linear-gradient(180deg,
      var(--sea-deep) 0%, var(--sea-mid) 35%, var(--sea-light) 62%,
      var(--foam) 74%, #dcd3c0 80%, var(--sand) 88%, var(--sand-dark) 100%);
  }

  .block { position: absolute; left: 0; right: 0; }
  .kicker { font-size: 19px; letter-spacing: 0.3px; }
  .hosts { font-family: "Kaushan Script", cursive; font-size: 40px; }
  .party-title {
    font-family: "Permanent Marker", cursive; font-size: 56px; color: var(--title);
    letter-spacing: 1px; text-transform: uppercase;
  }
  .rule { position: absolute; left: 80px; right: 80px; height: 2px; background: var(--text-light); opacity: .9; }
  .guests { font-family: "Sue Ellen Francisco", cursive; font-size: 34px; color: var(--text-dark); }
  .details { font-size: 19px; line-height: 25px; color: var(--text-dark); }
  .info { font-size: 20px; line-height: 26.5px; }
  .note { font-family: "Sue Ellen Francisco", cursive; font-size: 31px; line-height: 35px; color: var(--text-dark); }
  .rsvp { font-size: 14.5px; line-height: 20px; color: var(--text-dark); }

  .card--single .kicker { font-size: 16px; }
  .card--single .hosts { font-size: 34px; }
  .card--single .party-title { font-size: 50px; }
  .card--single .guests { font-size: 28px; }
  .card--single .details { font-size: 16px; line-height: 18px; color: var(--text-light); }
  .card--single .bring { font-size: 14.5px; line-height: 17px; color: var(--text-dark); }
  .fine { position: absolute; font-size: 12px; line-height: 14px; color: var(--text-dark); }
  .fine--left { left: 10px; top: 313px; text-align: left; }
  .fine--right { right: 10px; top: 285px; text-align: right; }
</style>
</head>
<body>
<main class="canvas">

  <section class="card card--front">
    <div class="beach-scene" role="img" aria-label="Aerial photo of turquoise ocean and waves washing onto a sandy beach"></div>
    <p class="block kicker" style="top:33px">LEAVE THE KIDS AT HOME AND LET YOUR HAIR DOWN AT</p>
    <p class="block hosts" style="top:70px">Simon &amp; Lorna's</p>
    <h1 class="block party-title" style="top:126px">Yuletide Unwind Bash</h1>
    <div class="rule" style="top:210px"></div>
    <p class="block guests" style="top:228px">for Marlow Heights and friends</p>
    <p class="block details" style="top:300px">SATURDAY 2 JANUARY FROM 6PM ‘TIL LATE<br>12 TIDEWATER STREET, MARLOW HEIGHTS</p>
  </section>

  <section class="card card--back">
    <div class="beach-scene" role="img" aria-label="Aerial photo of turquoise ocean and waves washing onto a sandy beach"></div>
    <p class="block info" style="top:32px">CHILD-FREE EVENT<br>DRESS: SUMMER CASUAL, BARE FEET WELCOME<br>COCKTAIL FOOD PROVIDED<br>BYO BUT ONLY IF YOU INSIST</p>
    <div class="rule" style="top:168px"></div>
    <p class="block note" style="top:200px">If you have some friends or neighbours that you like to<br>hang out with, we would love to meet. Bring them with you!</p>
    <p class="block rsvp" style="top:296px">AN RSVP FOR CATERING WOULD BE NICE.<br>TEXT SIMON XXX XXXXXX OR LORNA YYY YYYYY BEFORE XMAS PLEASE.</p>
  </section>

  <section class="card card--single">
    <div class="beach-scene" role="img" aria-label="Aerial photo of turquoise ocean and waves washing onto a sandy beach"></div>
    <p class="block kicker" style="top:10px">LEAVE THE KIDS AT HOME AND LET YOUR HAIR DOWN AT</p>
    <p class="block hosts" style="top:34px">Simon &amp; Lorna's</p>
    <h2 class="block party-title" style="top:82px">Yuletide Unwind Bash</h2>
    <div class="rule" style="top:158px; left:90px; right:90px"></div>
    <p class="block guests" style="top:166px">for Marlow Heights and friends</p>
    <p class="block details" style="top:213px">SATURDAY 2 JANUARY FROM 6PM ‘TIL LATE<br>12 TIDEWATER STREET, MARLOW HEIGHTS</p>
    <p class="block bring" style="top:254px">IF YOU HAVE SOME FRIENDS OR NEIGHBOURS THAT YOU LIKE TO<br>HANG OUT WITH, WE WOULD LOVE TO MEET. BRING THEM WITH YOU!</p>
    <p class="fine fine--left">AN RSVP FOR CATERING WOULD BE NICE.<br>TEXT SIMON XXX XXXXXX OR LORNA YYY YYYYY<br>BEFORE XMAS PLEASE.</p>
    <p class="fine fine--right">CHILD-FREE EVENT<br>DRESS: SUMMER CASUAL<br>BARE FEET WELCOME<br>COCKTAIL FOOD PROVIDED<br>BYO BUT ONLY IF YOU INSIST</p>
  </section>

</main>
</body>
</html>
```